Webdesign für Stahl- und Brückenbauunternehmen
Zielgruppe
Wir haben 180 Jahre Erfahrung im Stahl- und Brückenbau.
Unsere Auftraggeber ist die öffentliche Hand.
Aufgabenstellung
Das ODLA / TKU-Logo soll mit rein (siehe jetzige Webseite)

```html
<!DOCTYPE html>
<html lang="de">
<head>
<meta charset="utf-8">
<title>Travek – Stahl- und Brückenbau</title>
<link rel="stylesheet" href="https://fonts.googleapis.com/css2?family=Merriweather:wght@700&family=Open+Sans:wght@400;600;700&display=swap">
<style>
  :root{
    --blue:#0a7ad0;
    --dark:#3b3b3c;
    --dark-2:#474748;
    --white:#ffffff;
    --ink:#2c2c2c;
    --muted:#5a5a5a;
    --eu-blue:#1f3f9c;
    --sky-top:#7fa9cf;
    --sky-bottom:#c9c4b4;
  }
  *{margin:0;padding:0;box-sizing:border-box}
  html,body{width:1200px;height:894px;overflow:hidden;background:var(--white)}
  body{font-family:"Open Sans",Arial,sans-serif;color:var(--ink);position:relative}

  .site-header{position:absolute;left:0;top:0;width:1200px;height:90px;background:var(--white);z-index:3}
  .brand{position:absolute;left:66px;top:24px;display:flex;align-items:center;gap:8px;font-weight:700;font-size:28px;color:var(--blue);letter-spacing:.5px}
  .brand-square{width:14px;height:14px;background:var(--blue)}
  .main-nav{position:absolute;left:343px;top:34px;display:flex;gap:28px;font-size:13px;color:var(--muted)}
  .funding{position:absolute;left:991px;top:12px;display:flex;align-items:center;gap:18px}
  .funding-flag{width:49px;height:40px;background:var(--eu-blue)}
  .funding-marks{display:flex;flex-direction:column;font-size:14px;font-weight:600;color:var(--eu-blue);line-height:16px;letter-spacing:1px;margin-left:48px}

  .hero-strip{position:absolute;left:0;top:90px;width:1200px;height:83px;background:linear-gradient(90deg,var(--dark) 40%,#5e5e5e 100%)}

  .hero-panel{position:absolute;left:0;top:90px;width:537px;height:653px;background:linear-gradient(120deg,var(--dark) 0%,var(--dark-2) 60%,var(--dark) 100%)}
  .hero-panel::after{content:"";position:absolute;left:350px;top:0;width:187px;height:170px;background:rgba(255,255,255,.06)}
  .hero-title{position:absolute;left:69px;top:229px;font-family:"Merriweather",Georgia,serif;font-weight:700;font-size:32px;line-height:50px;color:var(--white)}
  .hero-text{position:absolute;left:69px;top:370px;font-size:12.5px;line-height:22px;color:#e6e6e6}
  .hero-button{position:absolute;left:72px;top:469px;width:155px;height:66px;background:var(--blue);color:var(--white);font-size:11px;letter-spacing:2px;display:flex;align-items:center;justify-content:center;gap:8px}

  .hero-photo{position:absolute;left:537px;top:173px;width:663px;height:721px;background:linear-gradient(180deg,var(--sky-top) 0%,#b7cbdc 40%,var(--sky-bottom) 65%,#6b6a60 100%)}

  .experience{position:absolute;left:566px;top:698px;width:125px;height:164px;background:var(--white);text-align:center;z-index:2}
  .experience-number{font-size:50px;font-weight:600;color:var(--blue);margin-top:14px;line-height:60px}
  .experience-label{font-size:11px;letter-spacing:1px;color:var(--blue);line-height:17px;margin-top:14px}

  .slider-nav{position:absolute;left:270px;top:825px;display:flex;align-items:baseline;gap:34px;color:var(--ink)}
  .slider-count{font-size:30px;font-weight:400}
  .slider-count small{font-size:14px}
</style>
</head>
<body>
  <header class="site-header">
    <div class="brand"><span class="brand-square"></span>Travek</div>
    <nav class="main-nav">
      <span>Unternehmen</span><span>Leistungen</span><span>Aktuelle Projekte</span><span>Referenzen</span><span>Kontakt</span>
    </nav>
    <div class="funding">
      <div class="funding-flag" role="img" aria-label="Förderhinweis"></div>
      <div class="funding-marks"><span>ODLA</span><span>TKU</span></div>
    </div>
  </header>

  <div class="hero-strip"></div>
  <section class="hero-panel">
    <h1 class="hero-title">Ihr Spezialist für<br>anspruchsvolle Projekte</h1>
    <p class="hero-text">180-jährige traditionsreiche Vergangenheit und<br>Erfahrung im Stahl- und Brückenbau</p>
    <a class="hero-button">MEHR INFO
      <svg width="14" height="8" viewBox="0 0 14 8"><path d="M0 4h13M10 1l3 3-3 3" stroke="#fff" stroke-width="1.2" fill="none"/></svg>
    </a>
  </section>

  <div class="hero-photo" role="img" aria-label="Foto einer stählernen Bogenbrücke vor Hochhäusern unter blauem Himmel"></div>

  <div class="experience">
    <div class="experience-number">180</div>
    <div class="experience-label">JAHRE<br>ERFAHRUNG</div>
  </div>

  <div class="slider-nav">
    <svg width="24" height="10" viewBox="0 0 24 10"><path d="M24 5H1M5 1L1 5l4 4" stroke="#2c2c2c" stroke-width="1.3" fill="none"/></svg>
    <span class="slider-count">2<small> / 3</small></span>
    <svg width="24" height="10" viewBox="0 0 24 10"><path d="M0 5h23M19 1l4 4-4 4" stroke="#2c2c2c" stroke-width="1.3" fill="none"/></svg>
  </div>
</body>
</html>
```